PTA Business Card

Seeking design for a business card, standard size. It is going to be for myself in regards to PTA - details:

Hollis Fernway Elementary School
PTA President
Neil Brawley
555-208-3147
Brawl1984@mailnest.example

Requirement:
Facebook icon? "Hollis Fernway PTA Durn"
Twitter thing? I am new to twitter so not sure what to put, here is the link:
https://twitter.com/HFRoverbirdsPTA

I was thinking on the front would be a notebook paper background? Not a requirement but was thinking it would look cool?

Total freedom here, let your creativity spread because I don't have any suggestions for design, sorry. Colors of school district are black and yellow.

Backside I am not sure exactly what to put on it.

```html
<!DOCTYPE html>
<html lang="en">
<head>
<meta charset="utf-8">
<title>Hollis Fernway Elementary PTA – Business Card</title>
<link rel="stylesheet" href="https://fonts.googleapis.com/css2?family=Arimo&family=Marcellus&family=Marcellus+SC&display=swap">
<style>
  :root {
    --backdrop-top: #e4e4e4;
    --backdrop-bottom: #a9a7a5;
    --paper-white: #fbfbfc;
    --rule-blue: #c9d3e6;
    --ink: #111111;
    --school-yellow-light: #f9f6cf;
    --school-yellow: #f2efb8;
    --band-black: #050505;
    --band-text: #ffffff;
    --square-grey: #5a5a5a;
  }
  * { margin: 0; padding: 0; box-sizing: border-box; }
  html, body { width: 1200px; height: 864px; overflow: hidden; }
  body {
    background: linear-gradient(160deg, var(--backdrop-top) 0%, var(--backdrop-bottom) 100%);
    position: relative;
  }
  .card {
    position: absolute;
    width: 520px;
    height: 298px;
    top: 283px;
    box-shadow: 0 6px 18px rgba(0,0,0,0.22);
    overflow: hidden;
  }

  /* Front: notebook paper */
  .card-front {
    left: 60px;
    background-color: var(--paper-white);
    background-image: repeating-linear-gradient(
      to bottom,
      transparent 0px,
      transparent 17px,
      var(--rule-blue) 17px,
      var(--rule-blue) 18px
    );
    text-align: center;
    color: var(--ink);
    padding-top: 40px;
  }
  .school-name {
    font-family: "Marcellus", serif;
    font-size: 27px;
    font-weight: 400;
    letter-spacing: 0.2px;
    white-space: nowrap;
  }
  .member-name {
    font-family: "Marcellus SC", serif;
    font-size: 24px;
    letter-spacing: 1.5px;
    margin-top: 12px;
    line-height: 1;
  }
  .member-role {
    font-family: "Arimo", sans-serif;
    font-size: 14px;
    margin-top: 2px;
  }
  .contact-list {
    list-style: none;
    font-family: "Arimo", sans-serif;
    font-size: 18px;
    line-height: 22px;
    margin-top: 16px;
    white-space: nowrap;
  }

  /* Back: school yellow with social band */
  .card-back {
    left: 620px;
    background: linear-gradient(135deg, var(--school-yellow-light) 0%, var(--school-yellow) 100%);
  }
  .card-back .school-name {
    position: absolute;
    top: 108px;
    left: 0;
    width: 100%;
    text-align: center;
    color: var(--ink);
  }
  .social-band {
    position: absolute;
    left: 0;
    bottom: 0;
    width: 100%;
    height: 46px;
    background: var(--band-black);
    display: flex;
    align-items: center;
    padding-left: 32px;
    gap: 28px;
  }
  .social-mark {
    width: 22px;
    height: 22px;
    background: var(--square-grey);
    flex: none;
  }
  .social-link {
    font-family: "Arimo", sans-serif;
    font-size: 17px;
    color: var(--band-text);
    white-space: nowrap;
  }
</style>
</head>
<body>
  <section class="card card-front" aria-label="Business card front">
    <h1 class="school-name">Hollis Fernway Elementary School</h1>
    <p class="member-name">Neil Brawley</p>
    <p class="member-role">PTA President</p>
    <ul class="contact-list">
      <li>555-208-3147</li>
      <li>Brawl1984@mailnest.example</li>
      <li>https://chirpline.example/HFRoverbirdsPTA</li>
    </ul>
  </section>

  <section class="card card-back" aria-label="Business card back">
    <h2 class="school-name">Hollis Fernway Elementary School</h2>
    <div class="social-band">
      <span class="social-mark" aria-hidden="true"></span>
      <span class="social-link">Hollis-Fernway-Elementary-PTA/508217364019283</span>
    </div>
  </section>
</body>
</html>
```